Drumbeat Winters (The Tale of a Young Meridian Rifleman)

We are looking for a poster design for what amounts to a 20 x 30 MOVIE POSTER - The time period of this story is just before and after the Harrowmark Frontier War - So think between 1860 and 1865 - Our story centers around a teen living in New York who runs off to join the Meridian Army (North - Blue) and engages in various battles vs the Bramwold Army (South - Grey) - We would like something that brings in all these elements PLUS Cornelius Whitby. The mini-series is based on the journal/letters of the main character so maybe that can be included on the poster as well.

We want to see which designer can be bold and creative - Questions??? Just ask and we will guide you! At the bottom of the poster we need:

By: Dorian P. Voss and Milo T. Brandquist

Target Market(s)

This project is being developed and presented to Executives at KVZ for a Mini-Series

Industry/Entity Type

Film Production

Other font styles liked:
• Designer Choice

Requirements
Must have
• THE TITLE OF THE STORY "Drumbeat Winters"
• Our story centers on an 18 year old boy who joins the Meridian Army (North) in New York and goes to war against the South (Bramwold Army)
• By: Dorian P. Voss and Milo T. Brandquist
Nice to have
• American Flag 1860
• Subdued Image of President Cornelius Whitby
• Journal or old fashioned handwritten letter

```html
<!DOCTYPE html>
<html lang="en">
<head>
<meta charset="utf-8">
<title>Drumbeat Winters — Poster</title>
<link rel="stylesheet" href="https://fonts.googleapis.com/css2?family=Bebas+Neue&family=Oswald:wght@400;500&display=swap">
<style>
  :root {
    --paper: #e9d7b0;
    --paper-dark: #c9a678;
    --stripe-red: #c9794a;
    --stripe-cream: #eadcbc;
    --ink-red: #a81f26;
    --ink-blue: #26336e;
    --credit: #f6ecd3;
    --canton: #8c7a5c;
    --edge-blue: #8d96a4;
  }
  html, body {
    margin: 0;
    padding: 0;
    width: 810px;
    height: 1200px;
    overflow: hidden;
    background: var(--paper);
  }
  .poster {
    position: relative;
    width: 810px;
    height: 1200px;
    overflow: hidden;
    background:
      linear-gradient(90deg, rgba(255,255,255,0) 80%, rgba(141,150,164,.55) 100%),
      radial-gradient(ellipse at 55% 40%, rgba(255,240,210,.25), rgba(90,60,30,.35) 100%),
      repeating-linear-gradient(90deg,
        var(--stripe-red) 0 30px,
        #d9925f 30px 44px,
        var(--stripe-cream) 44px 74px,
        #e3cfa6 74px 88px);
  }
  .canton {
    position: absolute;
    left: 0;
    top: 560px;
    width: 420px;
    height: 640px;
    background: linear-gradient(180deg, rgba(140,122,92,.55), rgba(110,92,66,.85));
  }
  .canton svg { position: absolute; inset: 0; }
  .portrait {
    position: absolute;
    left: 160px;
    top: 575px;
    width: 370px;
    height: 625px;
    border-radius: 46% 46% 0 0 / 22% 22% 0 0;
    background: linear-gradient(180deg, rgba(120,95,70,.35), rgba(80,62,45,.55) 60%, rgba(70,55,40,.45));
  }
  .title {
    position: absolute;
    left: 14px;
    top: 8px;
    margin: 0;
    font-family: "Bebas Neue", "Oswald", sans-serif;
    font-weight: 400;
    font-size: 172px;
    line-height: .86;
    letter-spacing: 1px;
    opacity: .9;
  }
  .title span { display: block; }
  .title .red { color: var(--ink-red); }
  .title .blue { color: var(--ink-blue); }
  .credits {
    position: absolute;
    left: 16px;
    top: 436px;
    width: 500px;
    font-family: "Oswald", "Bebas Neue", sans-serif;
    color: var(--credit);
    font-size: 14px;
    line-height: 1;
    text-transform: uppercase;
  }
  .credit-line {
    display: flex;
    align-items: center;
    gap: 4px;
    white-space: nowrap;
    height: 21px;
  }
  .label {
    display: inline-block;
    font-size: 5px;
    line-height: 5.5px;
    max-width: 40px;
    white-space: normal;
    text-align: right;
  }
  .ratings {
    display: flex;
    align-items: center;
    gap: 10px;
    margin-top: 4px;
  }
  .sound-mark {
    display: flex;
    align-items: center;
    gap: 4px;
    font-size: 11px;
  }
  .sound-mark i {
    width: 11px; height: 11px;
    background: var(--credit);
    display: inline-block;
  }
  .rating-box {
    display: flex;
    flex-direction: column;
    gap: 2px;
  }
  .rating-box .shape {
    width: 150px; height: 9px;
    border: 1px solid var(--credit);
    box-sizing: border-box;
  }
  .rating-box small {
    font-size: 5px;
    line-height: 1;
  }
  .created-by {
    margin-top: 12px;
    font-size: 17px;
    line-height: 1.15;
    font-weight: 500;
  }
</style>
</head>
<body>
<main class="poster">
  <div class="canton">
    <svg width="420" height="640" viewBox="0 0 420 640" aria-hidden="true">
      <g fill="#e6d2a8" opacity=".5">
        <polygon points="40,90 45,104 60,104 48,113 52,127 40,118 28,127 32,113 20,104 35,104"/>
        <polygon points="130,60 135,74 150,74 138,83 142,97 130,88 118,97 122,83 110,74 125,74"/>
        <polygon points="40,210 45,224 60,224 48,233 52,247 40,238 28,247 32,233 20,224 35,224"/>
        <polygon points="40,330 45,344 60,344 48,353 52,367 40,358 28,367 32,353 20,344 35,344"/>
        <polygon points="130,300 135,314 150,314 138,323 142,337 130,328 118,337 122,323 110,314 125,314"/>
        <polygon points="40,450 45,464 60,464 48,473 52,487 40,478 28,487 32,473 20,464 35,464"/>
        <polygon points="130,420 135,434 150,434 138,443 142,457 130,448 118,457 122,443 110,434 125,434"/>
        <polygon points="40,570 45,584 60,584 48,593 52,607 40,598 28,607 32,593 20,584 35,584"/>
        <polygon points="130,540 135,554 150,554 138,563 142,577 130,568 118,577 122,563 110,554 125,554"/>
      </g>
    </svg>
  </div>

  <div class="portrait" role="img" aria-label="Subdued sepia portrait of President Cornelius Whitby blended into the flag"></div>

  <h1 class="title">
    <span class="red">Drumbeat</span>
    <span class="blue">Winters</span>
  </h1>

  <section class="credits">
    <div class="credit-line">Studio Name <span class="label">presents</span> "Party Night"</div>
    <div class="credit-line"><span class="label">a</span> Producers <span class="label">a film by</span> Script Writer <span class="label">starring</span> Actor One Actor Two</div>
    <div class="credit-line"><span class="label">music by</span> The Musician <span class="label">costume design</span> Designer Name <span class="label">edited by</span> Editors Name <span class="label">production design</span> Designers Name <span class="label">director of photography</span> Cinematographer</div>
    <div class="credit-line"><span class="label">executive producer</span> Ex Producer 1 Ex Producer 2 <span class="label">produced by</span> Producer One Producer 2 <span class="label">story by</span> Story Writer</div>
    <div class="credit-line"><span class="label">screenplay by</span> Screen Writer <span class="label">directed by</span> Director Name</div>
    <div class="ratings">
      <div class="sound-mark"><i></i>Sonora Sound</div>
      <div class="rating-box">
        <div class="shape"></div>
        <small>Some content may not suit young viewers</small>
      </div>
    </div>
    <p class="created-by">Created by Dorian P. Voss<br>and Milo T. Brandquist</p>
  </section>
</main>
</body>
</html>
```